Harbor Sushi & Steak Dinner Menu

I'm looking for a MENU design with a particular feel. I want to have a base template made that I can then use for future alterations to the menu; ie I can go in and change out different entrees as the menu changes but the template will remain the same. (Ideally it would be in an Apple Pages format.). Also ideally - dinner menu will occupy 2 pages 8.5 x 11. The restaurant's name is Harbor. It is a MODERN steak house that will also feature Sushi, a Raw Bar, Exquisite Cocktails and a sophisticated nightlife crowd. I have attached our LOGO, a secondary logo that we will be featuring throughout the project including on the menu cover (the gold U). Finally - I have attached the content that we would like to see. AGAIN - I REITERATE: High end dining and lounge atmosphere. A couple of restaurants / menus that I love are Morvendel in NYC and Pellucid Steakhouse in Long Island NY. Please do not duplicate - just trying to offer some suggestions.

Requirements
Must have
• A sophisticated and elegant feel without being stuffy or old.

```html
<!DOCTYPE html>
<html lang="en">
<head>
<meta charset="utf-8">
<title>Harbor Sushi &amp; Steak — Dinner Menu</title>
<link href="https://fonts.googleapis.com/css2?family=Lato:ital,wght@0,300;0,400;0,700;1,400&display=swap" rel="stylesheet">
<style>
  :root {
    --red: #e41f3b;
    --gold: #c9a24c;
    --ink: #1e1e1e;
    --black: #0d0d0d;
    --paper: #ffffff;
    --rule: #9a9a9a;
  }
  * { box-sizing: border-box; margin: 0; padding: 0; }
  html, body { width: 1200px; height: 768px; overflow: hidden; background: var(--paper); }
  body { position: relative; font-family: "Lato", Arial, sans-serif; color: var(--ink); }

  .page { position: absolute; background: var(--red); }
  .page--sushi { left: 13px; top: 9px; width: 574px; height: 745px; }
  .page--kitchen { left: 609px; top: 8px; width: 582px; height: 744px; }

  .sheet { position: absolute; left: 17px; top: 32px; right: 17px; bottom: 18px; background: var(--paper); }
  .sheet::after { content: ""; position: absolute; inset: 8px; border: 1.5px solid var(--gold); pointer-events: none; }

  .banner { position: absolute; top: 0; width: 198px; height: 120px; }
  .page--sushi .banner { left: 19px; }
  .page--kitchen .banner { left: 31px; }
  .banner svg { position: absolute; inset: 0; }
  .banner-name {
    position: absolute; left: 0; right: 0; top: 44px; text-align: center;
    font-weight: 400; font-size: 30px; letter-spacing: 3px; color: var(--gold);
  }

  .menu-title {
    position: absolute; top: 70px; font-weight: 400; font-size: 26px;
    letter-spacing: 0.5px; color: var(--gold);
  }
  .page--sushi .menu-title { left: 306px; }
  .page--kitchen .menu-title { left: 305px; }

  .section { position: absolute; display: flex; }
  .section-label {
    writing-mode: vertical-rl; transform: rotate(180deg);
    color: var(--red); font-size: 14px; letter-spacing: 1.2px; font-weight: 400;
    text-transform: uppercase; text-align: right; width: 18px; line-height: 17px;
    display: flex; align-items: center;
  }
  .section-label .gf { transform: rotate(90deg); margin-top: 3px; }
  .section-body { border-left: 1px solid var(--rule); margin-left: 6px; padding-left: 8px; }

  .item { margin-bottom: 6px; }
  .item-name { color: var(--gold); font-weight: 700; font-size: 10.5px; line-height: 13px; }
  .item-desc { font-style: italic; font-size: 7.3px; line-height: 9px; color: var(--ink); }
  .item-name .inline { color: var(--ink); font-weight: 400; font-style: italic; font-size: 7.3px; }

  .plain-list li { list-style: none; font-size: 10px; line-height: 17px; color: var(--ink); }
  .plain-list .item-desc { margin-top: 2px; margin-bottom: 8px; }

  .two-col { display: grid; grid-template-columns: 94px 94px; column-gap: 6px; }

  .gf {
    display: inline-flex; align-items: center; justify-content: center;
    width: 9px; height: 9px; border-radius: 50%; background: var(--red);
    color: var(--paper); font-size: 4.5px; font-weight: 700; font-style: normal;
    vertical-align: middle; margin-left: 2px; writing-mode: horizontal-tb;
  }
  .gf--lg { width: 12px; height: 12px; font-size: 5.5px; }

  .sides-list { font-size: 10px; line-height: 16px; }
  .sides-grid { display: grid; grid-template-columns: 106px 120px; }
  .sides-grid span { line-height: 16px; }
</style>
</head>
<body>

<!-- Page one: sushi and raw bar -->
<section class="page page--sushi" role="img" aria-label="Red wave pattern border">
  <div class="sheet"></div>
  <div class="banner">
    <svg width="198" height="120" viewBox="0 0 198 120"><polygon points="0,0 198,0 198,104 0,120" fill="var(--black)"/></svg>
    <div class="banner-name">HARBOR</div>
  </div>
  <h1 class="menu-title">DINNER MENU</h1>

  <div class="section" style="left:58px; top:162px; height:136px;">
    <div class="section-label">Sushi / Sashimi <span class="gf gf--lg">GF</span></div>
    <div class="section-body two-col" style="grid-template-columns:94px 90px;">
      <div>
        <div class="item"><div class="item-name">Toro</div><div class="item-desc">Blue Fin Tuna Belly</div></div>
        <div class="item"><div class="item-name">Unagi</div><div class="item-desc">Fresh Water Eel</div></div>
        <div class="item"><div class="item-name">Ebi</div><div class="item-desc">Cooked Shrimp</div></div>
        <div class="item"><div class="item-name">Sake</div><div class="item-desc">Salmon</div></div>
        <div class="item"><div class="item-name">Hamachi</div><div class="item-desc">Yellowtail</div></div>
      </div>
      <div>
        <div class="item"><div class="item-name">Madai</div><div class="item-desc">Red Snapper</div></div>
        <div class="item"><div class="item-name">Uni</div><div class="item-desc">Sea Urchin</div></div>
        <div class="item"><div class="item-name">Maguro</div><div class="item-desc">Tuna</div></div>
        <div class="item"><div class="item-name">Hirame</div><div class="item-desc">Fluke</div></div>
      </div>
    </div>
  </div>

  <div class="section" style="left:58px; top:326px; height:119px;">
    <div class="section-label">Sushi Platters</div>
    <div class="section-body" style="width:160px;">
      <div class="item"><div class="item-name">Small <span class="gf">GF</span></div><div class="item-desc">Five Pieces Assorted Sushi,<br>Nine Pieces Sashimi,<br>Spicy Tuna Roll</div></div>
      <div class="item"><div class="item-name">Large <span class="gf">GF</span></div><div class="item-desc">Eight Pieces Assorted Sushi,<br>Eighteen Pieces Of Sashimi,<br>Alaskan Roll,<br>Rainbow Roll</div></div>
    </div>
  </div>

  <div class="section" style="left:58px; top:469px; height:190px;">
    <div class="section-label">Classic Rolls</div>
    <div class="section-body" style="width:170px;">
      <div class="item"><div class="item-name">Yellowtail <span class="gf">GF</span></div><div class="item-desc">Inside Out Roll With Scallions, Spicy Tuna or Salmon or Yellowtail, Spicy Mayo</div></div>
      <div class="item"><div class="item-name">California <span class="gf">GF</span></div><div class="item-desc">Crab Meat, Cucumber and Avocado</div></div>
      <div class="item"><div class="item-name">Vegetable <span class="gf">GF</span></div><div class="item-desc">Avocado, Cucumber, Asparagus &amp; Pickled Reddish</div></div>
      <div class="item"><div class="item-name">Spider</div><div class="item-desc">Soft Shell Crab &amp; Avocado With Eel Sauce</div></div>
      <div class="item"><div class="item-name">Shrimp Tempura</div><div class="item-desc">Deep Fried Tempura Shrimp and Eel Sauce</div></div>
      <div class="item"><div class="item-name">Alaskan <span class="gf">GF</span></div><div class="item-desc">Salmon and Avocado</div></div>
    </div>
  </div>

  <div class="section" style="left:274px; top:162px; height:222px;">
    <div class="section-label">Special Rolls</div>
    <div class="section-body" style="width:210px;">
      <div class="item"><div class="item-name">The Harbor</div><div class="item-desc">Tuna, Salmon, Yellowtail, Avocado, Spicy Mayo, Soy Bean Paper</div></div>
      <div class="item"><div class="item-name">King Crab Rainbow</div><div class="item-desc">King Crab, Avocado, Cucumbers, Assorted Fish on Top</div></div>
      <div class="item"><div class="item-name">Empress</div><div class="item-desc">Shrimp Tempura, Spicy Tuna On Top, Eel Sauce, Spicy Mayo</div></div>
      <div class="item"><div class="item-name">Spicy Girl</div><div class="item-desc">Spicy Crunchy Crab Meat, Cucumber, Shrimp on Top</div></div>
      <div class="item"><div class="item-name">Dragon</div><div class="item-desc">Eel, Cucumber, Avocado, And Tobiko on Top, Eel Sauce</div></div>
      <div class="item"><div class="item-name">Yummy</div><div class="item-desc">Spicy Crunchy Salmon, Avocado, Mango And Salmon on Top</div></div>
      <div class="item"><div class="item-name">No. 9</div><div class="item-desc">Shrimp Tempura, Avocado, Kani, Spicy Mayo, Tobiko</div></div>
      <div class="item"><div class="item-name">Sunrise Roll</div><div class="item-desc">Spicy Crunchy Tuna And Avocado, Spicy Crunchy Salmon on Top</div></div>
    </div>
  </div>

  <div class="section" style="left:274px; top:431px; height:141px;">
    <div class="section-label">Seafood Raw Bar</div>
    <div class="section-body">
      <ul class="plain-list">
        <li>Lobster Cocktail</li>
        <li>Shrimp Cocktail</li>
        <li>Clams on the Half Shell</li>
        <li>Oysters on the Half Shell</li>
        <li>Colossal Crab Cocktail</li>
        <li style="margin-top:3px; line-height:13px;">Raw Bar Plate for One
          <div class="item-desc" style="font-style:normal; font-size:7.5px;">Two Shrimp, Half of a One Pound Lobster,<br>Two Clams, One East Coast Oyster,<br>One West Coast Oyster</div></li>
      </ul>
    </div>
  </div>

  <div class="section" style="left:274px; top:600px; height:73px;">
    <div class="section-label">Seafood Platters <span class="gf gf--lg">GF</span></div>
    <div class="section-body">
      <div class="item-desc" style="margin-top:2px;">Shrimp, Oysters, Clams, Lobster and Crab</div>
      <ul class="plain-list" style="margin-top:5px;"><li>Large / Colossal</li></ul>
    </div>
  </div>
</section>

<!-- Page two: kitchen -->
<section class="page page--kitchen" role="img" aria-label="Red wave pattern border">
  <div class="sheet"></div>
  <div class="banner">
    <svg width="198" height="120" viewBox="0 0 198 120"><polygon points="0,0 198,0 198,104 0,120" fill="var(--black)"/></svg>
    <div class="banner-name">HARBOR</div>
  </div>
  <h1 class="menu-title">DINNER MENU</h1>

  <div class="section" style="left:56px; top:130px; height:461px;">
    <div class="section-label" style="align-items:flex-end; justify-content:flex-end;">Appetizer</div>
    <div class="section-body" style="width:196px;">
      <div class="item"><div class="item-name">BAO Bun</div><div class="item-desc">Hoisin BBQ Pancetta Cut Pork Loin, Crispy Onions, Micro Mint</div></div>
      <div class="item"><div class="item-name">Five Spice Crispy Popcorn Crusted</div></div>
      <div class="item"><div class="item-name">Prawns (2)</div><div class="item-desc">Classic Burre Blanc</div></div>
      <div class="item"><div class="item-name">Jumbo Lump Crab</div><div class="item-desc">Citrus Miso Drizzle, Spring Pea Puree, Micro Greens</div></div>
      <div class="item"><div class="item-name">Crispy Wonton Napoleon</div><div class="item-desc">Cucumber Gallete, Ahi Tuna, Jumbo Lump Crab Meat, Wasabi Aioli, Shoestring Wontons</div></div>
      <div class="item"><div class="item-name">PEI Mussels</div><div class="item-desc">Charred Artichoke Hearts, Blistered Heirloom Tomatoes, Garlic White Wine Broth</div></div>
      <div class="item"><div class="item-name">New Zealand / Domestic Small Eye</div></div>
      <div class="item"><div class="item-name">Lamb Chop (1) <span class="inline">Crispy Porcini Risotto Cake</span></div></div>
      <div class="item"><div class="item-name">Classic Wedge</div><div class="item-desc">Bleu Cheese, Bacon Lardons, Heirloom Tomatoes</div></div>
      <div class="item"><div class="item-name">Mixed Baby Greens</div><div class="item-desc">Heirloom Tomatoes, Cucumber, Red Onion, Dijon Vinaigrette</div></div>
      <div class="item"><div class="item-name">Tabulleh</div><div class="item-desc">Buckwheat Grain, Fresh Mint, Tomato Concasse, Cucumber, Parsley, Fresh Squeezed Lemon, EVOO., Salt and Pepper</div></div>
      <div class="item"><div class="item-name">Tomato Mozzarella Salad / Burratta</div></div>
      <div class="item"><div class="item-name">Spinach Salad</div><div class="item-desc">Green Apple, Feta, Currants, with Per-simmons Vinaigrette</div></div>
      <div class="item"><div class="item-name">Kale Caesar</div><div class="item-desc">Homemade Cacio E'peppe Dressing, Pecorino and Parmesan Cheese, Toasted Croutons</div></div>
    </div>
  </div>

  <div class="section" style="left:56px; top:600px; height:80px;">
    <div class="section-label">Sauces</div>
    <div class="section-body">
      <ul class="plain-list" style="line-height:16px;">
        <li style="line-height:16px;">Cabernet Demi Glaz</li>
        <li style="line-height:16px;">Gorganzola Brulle Cream</li>
        <li style="line-height:16px;">Truffled Wild Mushroom Ragu</li>
        <li style="line-height:16px;">Horseradish Cream</li>
        <li style="line-height:16px;">House Steak Sauce</li>
      </ul>
    </div>
  </div>

  <div class="section" style="left:272px; top:130px; height:300px;">
    <div class="section-label" style="align-items:flex-end; justify-content:flex-end;">Entrees</div>
    <div class="section-body" style="width:214px;">
      <div class="item"><div class="item-name">Pan Roasted Miso Glazed Black Cod</div><div class="item-desc">Green Tea Noodle Stir Fry, Napa Cabbage, Carrot, Japanese Eggplant</div></div>
      <div class="item"><div class="item-name">Pan Seared Striped Bass</div><div class="item-desc">Lobster Succotash In A Tomato Saffron Broth</div></div>
      <div class="item"><div class="item-name">E.V.O.O. Salted / Grilled Swordfish</div><div class="item-desc">Sun Dried Tomato, Olive and Caper Tapenade, Over Basmati Rice</div></div>
      <div class="item"><div class="item-name">Grilled Half Chicken</div><div class="item-desc">Sun Dried Tomato And Basil Israeli Cous-cous, Pan Au Jus</div></div>
      <div class="item"><div class="item-name">Roasted Fresh Caviatelle Ratatoille</div><div class="item-desc">Vegetable Broth</div></div>
      <div class="item"><div class="item-name">Lobster Cartoccio</div><div class="item-desc">Shrimp, Mussels, Clams, Fresh Herb Tomato Broth, Tossed with Bucatini</div></div>
      <div class="item"><div class="item-name">Charred Artichoke Hearts <span class="gf">GF</span></div><div class="item-desc">Heirloom Tomatoes, Caper Berries, Spring Onions, Fresh Basil, White Wine Reduction Over Forbidden Rice</div></div>
      <div class="item"><div class="item-name">Mediterranean Grilled Veggie Plate <span class="gf">GF</span></div><div class="item-desc">Artichoke Hearts, Japanese Eggplant, Green &amp; White Asparagus, Seared Heirloom Tomatoes, Roasted Baby Carrots, Cauliflower Rice, Evoo &amp; Fig Drizzle</div></div>
    </div>
  </div>

  <div class="section" style="left:264px; top:436px; height:94px;">
    <div class="section-label" style="width:34px;">USDA Prime Steaks <span class="gf gf--lg">GF</span></div>
    <div class="section-body" style="margin-left:4px;">
      <ul class="plain-list">
        <li>10 Oz Filet</li>
        <li>14 or 16 oz New York Strip</li>
        <li>24 oz Boneless Ribeye</li>
        <li>36 oz Bone in Rib Eye</li>
        <li>Berkshire Pork Chop</li>
      </ul>
    </div>
  </div>

  <div class="section" style="left:272px; top:553px; height:127px;">
    <div class="section-label">Sides</div>
    <div class="section-body sides-list">
      <div>Mashed Idaho Potatoes</div>
      <div style="line-height:12px; margin:3px 0 2px;">Bacon, Sweet Corn, Caramelized<br>Vidalia Onion fingerling potatoes</div>
      <div>Roasted Peanut Potatoes</div>
      <div>Creamed Spinach</div>
      <div class="sides-grid">
        <span>Sautéed Spinach</span><span>Israeli Cous Cous</span>
        <span>Grilled Asparagus</span><span>Sweet Potato Steak Fries</span>
        <span>French Beans</span><span>Corn Skillet</span>
      </div>
    </div>
  </div>
</section>

</body>
</html>
```